Multiple bag designs for poultry pellets

Terravane require a set of (x6) new bag designs for our 25kg poultry pellets. The bags must have 'made in the UK' and '100% organic' on the front of the design. An example of the current bag label is uploaded. A sketch of the requirements is also uploaded. Each design will require a different colour to make differentiation between bags. The final design must have space similar to the original for product information (i.e. the product specification). The bag brand should be Grovita - KB45

The front design should either utilise prominent cultural landmarks (UK & Ireland) as line drawings (e.g. Old Hesk etc). or utilisation of the following crops as either pictures or drawings:

Durian Fruit
Dragon fruit
Coffee
Rice
Banana
Sugar cane

Pictures could also depict Vietnam Agri landscapes

Target Market(s)

Organic farmers in Asia

Industry/Entity Type

Organic fertilisers

Font styles to use
Serif

Colors

Designer to choose colors to be used in the design.

Requirements
Must have
• 6 designs, based on the same theme (i.e colour, picture or pattern), must include 'made in uk' and '100% organic'
Nice to have
• A nod to poultry, i.e. chicken or the fact these are pellets (picture or line drawing)

```html
<!DOCTYPE html>
<html lang="en">
<head>
<meta charset="utf-8">
<title>Grovita - KB45 · Terravane bag range</title>
<link href="https://fonts.googleapis.com/css2?family=Archivo:wght@400;600;800;900&display=swap" rel="stylesheet">
<style>
  :root{
    --page:#ffffff;
    --cream:#f3f0e4;
    --white:#fdfdfb;
    --green:#6ea62c;
    --brand:#4a3424;
    --red:#d8261f;
    --ink:#3a3a3a;
    --card-line:#9a9a9a;
    --durian:#f2ba8c;
    --dragon:#e8a6b9;
    --coffee:#b9977b;
    --rice:#3f9b94;
    --banana:#f4e84a;
    --cane:#b6c35c;
  }
  *{box-sizing:border-box;margin:0;padding:0}
  html,body{width:1200px;height:1200px;overflow:hidden;background:var(--page)}
  body{position:relative;font-family:"Archivo",Arial,sans-serif;color:var(--ink)}

  .bag{position:absolute;width:340px;height:485px;border-radius:4px;overflow:hidden;background:var(--cream)}
  .bag--durian{left:40px;top:70px;--tone:var(--durian);--title:var(--green)}
  .bag--dragon{left:425px;top:70px;--tone:var(--dragon);--title:var(--green)}
  .bag--coffee{left:820px;top:70px;--tone:var(--coffee);--title:#fff}
  .bag--rice{left:40px;top:640px;--tone:var(--rice);--title:#fff}
  .bag--banana{left:425px;top:640px;--tone:var(--banana);--title:var(--green)}
  .bag--cane{left:820px;top:640px;--tone:var(--cane);--title:var(--green)}

  .bag__top{position:absolute;left:0;top:0;width:100%;height:110px;background:var(--tone)}
  .bag__title{position:absolute;left:0;top:66px;width:100%;text-align:center;font-weight:800;font-size:24px;letter-spacing:1px;color:var(--title)}

  .organic{position:absolute;left:232px;top:104px;width:96px;height:62px}
  .organic__seal{position:absolute;left:34px;top:0;width:30px;height:30px;border-radius:50%;background:var(--red)}
  .organic__label{position:absolute;left:0;top:35px;width:96px;height:14px;border-radius:7px;background:var(--red);color:#fff;font-size:8px;font-weight:600;text-align:center;line-height:14px}

  .crop{position:absolute;left:36px;top:165px;width:140px;height:150px}
  .crop__art{width:140px;height:120px;border-radius:10px}
  .crop__name{font-size:8px;font-weight:600;color:#222;margin-top:8px;margin-left:10px}
  .bag--durian .crop__art{background:radial-gradient(circle at 45% 50%,#8e8e86,#d9d8d0 75%)}
  .bag--dragon .crop__art{background:radial-gradient(circle at 55% 55%,#b9b9b5,#e2e1dc 75%)}
  .bag--coffee .crop__art{background:radial-gradient(circle at 50% 50%,#8f8a84,#dedbd4 75%)}
  .bag--rice .crop__art{background:radial-gradient(circle at 40% 40%,#a7a69e,#e1dfd6 75%)}
  .bag--banana .crop__art{background:radial-gradient(circle at 45% 50%,#9d9b94,#dfddd5 75%)}
  .bag--cane .crop__art{background:radial-gradient(circle at 50% 50%,#a3a49b,#e0e0d7 75%)}

  .spec{position:absolute;left:180px;top:170px;width:156px;height:168px;border:1px solid var(--card-line);border-radius:8px;background:#fff;padding:7px 8px;font-size:4.6px;line-height:1.45;color:#333}
  .spec h4{font-size:5px;font-weight:800;margin-top:3px}
  .spec p{margin:0}

  .waves{position:absolute;left:0;top:300px;width:340px;height:185px}

  .logo{position:absolute;left:36px;top:360px}
  .logo__name{font-weight:900;font-size:37px;line-height:0.92;color:var(--brand);letter-spacing:1px}
  .logo__tag{font-size:9.5px;font-weight:600;color:var(--green);letter-spacing:1.3px;margin-top:6px}

  .uk-seal{position:absolute;left:262px;top:370px;width:46px;height:46px;border-radius:50%;background:#e8ecf3;border:3px solid #2b3f8c}

  .weight{position:absolute;left:196px;top:420px;font-weight:800;color:#111}
  .weight__label{font-size:8px;font-weight:600;display:block}
  .weight__value{font-size:15px}
</style>
</head>
<body>

<!-- Durian -->
<section class="bag bag--durian">
  <div class="bag__top"></div>
  <h2 class="bag__title">GROVITA - KB45</h2>
  <div class="organic"><div class="organic__seal" role="img" aria-label="Rooster emblem"></div><div class="organic__label">100% Organic</div></div>
  <div class="crop"><div class="crop__art" role="img" aria-label="Line drawing of a durian fruit, whole and halved"></div><p class="crop__name">Durian Fruit</p></div>
  <div class="spec">
    <p><b>Organic Poultry Pellets</b></p><p>Complete feed for steady soil growth</p><p>Weight: 25kg</p><p>Form: pellet</p>
    <h4>Key features</h4><p>• Slow release nitrogen</p><p>• Rich in organic matter</p>
    <h4>Ingredients</h4><p>Composted poultry manure, plant meal, natural minerals</p><p>Usage: 100–150g per plant</p>
    <h4>Storage</h4><p>Keep dry and sealed, away from sunlight</p><p>Made by Terravane Agri Co. Ltd</p><p>MFD 01/2025 · EXP 01/2027</p>
  </div>
  <svg class="waves" viewBox="0 0 340 185" aria-hidden="true">
    <path d="M0 40 C110 0 220 60 340 10 L340 185 L0 185 Z" fill="var(--tone)"/>
    <path d="M0 58 C110 18 220 78 340 28 L340 185 L0 185 Z" fill="var(--green)"/>
    <path d="M0 70 C110 30 220 90 340 40 L340 185 L0 185 Z" fill="var(--white)"/>
    <rect x="0" y="155" width="340" height="30" fill="var(--tone)"/>
  </svg>
  <div class="logo"><div class="logo__name">TERRA<br>VANE</div><div class="logo__tag">NATURAL FERTILISER</div></div>
  <div class="uk-seal" role="img" aria-label="Made in UK seal"></div>
  <div class="weight"><span class="weight__label">Nt.Wt</span><span class="weight__value">25kg</span></div>
</section>

<!-- Dragon fruit -->
<section class="bag bag--dragon">
  <div class="bag__top"></div>
  <h2 class="bag__title">GROVITA - KB45</h2>
  <div class="organic"><div class="organic__seal" role="img" aria-label="Rooster emblem"></div><div class="organic__label">100% Organic</div></div>
  <div class="crop"><div class="crop__art" role="img" aria-label="Line drawing of a dragon fruit, whole and halved"></div><p class="crop__name">Dragon fruit</p></div>
  <div class="spec">
    <p><b>Organic Poultry Pellets</b></p><p>Complete feed for steady soil growth</p><p>Weight: 25kg</p><p>Form: pellet</p>
    <h4>Key features</h4><p>• Slow release nitrogen</p><p>• Rich in organic matter</p>
    <h4>Ingredients</h4><p>Composted poultry manure, plant meal, natural minerals</p><p>Usage: 100–150g per plant</p>
    <h4>Storage</h4><p>Keep dry and sealed, away from sunlight</p><p>Made by Terravane Agri Co. Ltd</p><p>MFD 01/2025 · EXP 01/2027</p>
  </div>
  <svg class="waves" viewBox="0 0 340 185" aria-hidden="true">
    <path d="M0 40 C110 0 220 60 340 10 L340 185 L0 185 Z" fill="var(--tone)"/>
    <path d="M0 58 C110 18 220 78 340 28 L340 185 L0 185 Z" fill="var(--green)"/>
    <path d="M0 70 C110 30 220 90 340 40 L340 185 L0 185 Z" fill="var(--white)"/>
    <rect x="0" y="155" width="340" height="30" fill="var(--tone)"/>
  </svg>
  <div class="logo"><div class="logo__name">TERRA<br>VANE</div><div class="logo__tag">NATURAL FERTILISER</div></div>
  <div class="uk-seal" role="img" aria-label="Made in UK seal"></div>
  <div class="weight"><span class="weight__label">Nt.Wt</span><span class="weight__value">25kg</span></div>
</section>

<!-- Coffee -->
<section class="bag bag--coffee">
  <div class="bag__top"></div>
  <h2 class="bag__title">GROVITA - KB45</h2>
  <div class="organic"><div class="organic__seal" role="img" aria-label="Rooster emblem"></div><div class="organic__label">100% Organic</div></div>
  <div class="crop"><div class="crop__art" role="img" aria-label="Line drawing of coffee beans and leaves"></div><p class="crop__name">Coffee</p></div>
  <div class="spec">
    <p><b>Organic Poultry Pellets</b></p><p>Complete feed for steady soil growth</p><p>Weight: 25kg</p><p>Form: pellet</p>
    <h4>Key features</h4><p>• Slow release nitrogen</p><p>• Rich in organic matter</p>
    <h4>Ingredients</h4><p>Composted poultry manure, plant meal, natural minerals</p><p>Usage: 100–150g per plant</p>
    <h4>Storage</h4><p>Keep dry and sealed, away from sunlight</p><p>Made by Terravane Agri Co. Ltd</p><p>MFD 01/2025 · EXP 01/2027</p>
  </div>
  <svg class="waves" viewBox="0 0 340 185" aria-hidden="true">
    <path d="M0 40 C110 0 220 60 340 10 L340 185 L0 185 Z" fill="var(--tone)"/>
    <path d="M0 58 C110 18 220 78 340 28 L340 185 L0 185 Z" fill="var(--green)"/>
    <path d="M0 70 C110 30 220 90 340 40 L340 185 L0 185 Z" fill="var(--white)"/>
    <rect x="0" y="155" width="340" height="30" fill="var(--tone)"/>
  </svg>
  <div class="logo"><div class="logo__name">TERRA<br>VANE</div><div class="logo__tag">NATURAL FERTILISER</div></div>
  <div class="uk-seal" role="img" aria-label="Made in UK seal"></div>
  <div class="weight"><span class="weight__label">Nt.Wt</span><span class="weight__value">25kg</span></div>
</section>

<!-- Rice -->
<section class="bag bag--rice">
  <div class="bag__top"></div>
  <h2 class="bag__title">GROVITA - KB45</h2>
  <div class="organic"><div class="organic__seal" role="img" aria-label="Rooster emblem"></div><div class="organic__label">100% Organic</div></div>
  <div class="crop"><div class="crop__art" role="img" aria-label="Line drawing of rice stalks with grain heads"></div><p class="crop__name">Rice</p></div>
  <div class="spec">
    <p><b>Organic Poultry Pellets</b></p><p>Complete feed for steady soil growth</p><p>Weight: 25kg</p><p>Form: pellet</p>
    <h4>Key features</h4><p>• Slow release nitrogen</p><p>• Rich in organic matter</p>
    <h4>Ingredients</h4><p>Composted poultry manure, plant meal, natural minerals</p><p>Usage: 100–150g per plant</p>
    <h4>Storage</h4><p>Keep dry and sealed, away from sunlight</p><p>Made by Terravane Agri Co. Ltd</p><p>MFD 01/2025 · EXP 01/2027</p>
  </div>
  <svg class="waves" viewBox="0 0 340 185" aria-hidden="true">
    <path d="M0 40 C110 0 220 60 340 10 L340 185 L0 185 Z" fill="var(--tone)"/>
    <path d="M0 58 C110 18 220 78 340 28 L340 185 L0 185 Z" fill="var(--green)"/>
    <path d="M0 70 C110 30 220 90 340 40 L340 185 L0 185 Z" fill="var(--white)"/>
    <rect x="0" y="155" width="340" height="30" fill="var(--tone)"/>
  </svg>
  <div class="logo"><div class="logo__name">TERRA<br>VANE</div><div class="logo__tag">NATURAL FERTILISER</div></div>
  <div class="uk-seal" role="img" aria-label="Made in UK seal"></div>
  <div class="weight"><span class="weight__label">Nt.Wt</span><span class="weight__value">25kg</span></div>
</section>

<!-- Banana -->
<section class="bag bag--banana">
  <div class="bag__top"></div>
  <h2 class="bag__title">GROVITA - KB45</h2>
  <div class="organic"><div class="organic__seal" role="img" aria-label="Rooster emblem"></div><div class="organic__label">100% Organic</div></div>
  <div class="crop"><div class="crop__art" role="img" aria-label="Line drawing of a bunch of bananas"></div><p class="crop__name">Banana</p></div>
  <div class="spec">
    <p><b>Organic Poultry Pellets</b></p><p>Complete feed for steady soil growth</p><p>Weight: 25kg</p><p>Form: pellet</p>
    <h4>Key features</h4><p>• Slow release nitrogen</p><p>• Rich in organic matter</p>
    <h4>Ingredients</h4><p>Composted poultry manure, plant meal, natural minerals</p><p>Usage: 100–150g per plant</p>
    <h4>Storage</h4><p>Keep dry and sealed, away from sunlight</p><p>Made by Terravane Agri Co. Ltd</p><p>MFD 01/2025 · EXP 01/2027</p>
  </div>
  <svg class="waves" viewBox="0 0 340 185" aria-hidden="true">
    <path d="M0 40 C110 0 220 60 340 10 L340 185 L0 185 Z" fill="var(--tone)"/>
    <path d="M0 58 C110 18 220 78 340 28 L340 185 L0 185 Z" fill="var(--green)"/>
    <path d="M0 70 C110 30 220 90 340 40 L340 185 L0 185 Z" fill="var(--white)"/>
    <rect x="0" y="155" width="340" height="30" fill="var(--tone)"/>
  </svg>
  <div class="logo"><div class="logo__name">TERRA<br>VANE</div><div class="logo__tag">NATURAL FERTILISER</div></div>
  <div class="uk-seal" role="img" aria-label="Made in UK seal"></div>
  <div class="weight"><span class="weight__label">Nt.Wt</span><span class="weight__value">25kg</span></div>
</section>

<!-- Sugar cane -->
<section class="bag bag--cane">
  <div class="bag__top"></div>
  <h2 class="bag__title">GROVITA - KB45</h2>
  <div class="organic"><div class="organic__seal" role="img" aria-label="Rooster emblem"></div><div class="organic__label">100% Organic</div></div>
  <div class="crop"><div class="crop__art" role="img" aria-label="Line drawing of sugar cane stalks and leaves"></div><p class="crop__name">Sugar cane</p></div>
  <div class="spec">
    <p><b>Organic Poultry Pellets</b></p><p>Complete feed for steady soil growth</p><p>Weight: 25kg</p><p>Form: pellet</p>
    <h4>Key features</h4><p>• Slow release nitrogen</p><p>• Rich in organic matter</p>
    <h4>Ingredients</h4><p>Composted poultry manure, plant meal, natural minerals</p><p>Usage: 100–150g per plant</p>
    <h4>Storage</h4><p>Keep dry and sealed, away from sunlight</p><p>Made by Terravane Agri Co. Ltd</p><p>MFD 01/2025 · EXP 01/2027</p>
  </div>
  <svg class="waves" viewBox="0 0 340 185" aria-hidden="true">
    <path d="M0 40 C110 0 220 60 340 10 L340 185 L0 185 Z" fill="var(--tone)"/>
    <path d="M0 58 C110 18 220 78 340 28 L340 185 L0 185 Z" fill="var(--green)"/>
    <path d="M0 70 C110 30 220 90 340 40 L340 185 L0 185 Z" fill="var(--white)"/>
    <rect x="0" y="155" width="340" height="30" fill="var(--tone)"/>
  </svg>
  <div class="logo"><div class="logo__name">TERRA<br>VANE</div><div class="logo__tag">NATURAL FERTILISER</div></div>
  <div class="uk-seal" role="img" aria-label="Made in UK seal"></div>
  <div class="weight"><span class="weight__label">Nt.Wt</span><span class="weight__value">25kg</span></div>
</section>

</body>
</html>
```